Flyer Design Project

I teach a spiritual dance class and I want to explain what it is and who it would benefit. I would love to have a sticker for where I am teaching it because that can change.

I want it to be a bit spiritual, very hip and cool, and transformational!!

Target Market(s)

Mostly women (or enlightened men)! all ages

Requirements
Must have
• Tidal Sway

We need to move. We need to breathe. We need to smile and giggle and laugh and cry and scream and make noise and dance. It's not about burning calories and it is not about reaching a goal. It's about feeling. It's about taking the time to nurture our souls. It's about finding joy and peace in our hectic lives. It's about healing.

Tidal Sway is a wildly fun, uplifting, emotionally cleansing, refreshing, restorative, heart-opening, transformational dance celebration that is sure to leave you relaxed and smiling. All ages, shapes and sizes are welcome with no experience necessary.
About Nora:

I was certified at Venduro in both “Move Through Morning” and “Orbit Motion” and am a
certified Group Exercise Instructor with the Cardio and Wellness Guild of Northland (CWGN). I also have a black belt in Tae Kwon Do. As of 2013, I will be a certified holistic health and nutrition coach and am the creator of the popular Bright, Brisk, and Bold page on Chatterbook.
For more info:
Noradekker@mailquill.com

Classes and workshops to energize your body, mind, and spirit.

```html
<!DOCTYPE html>
<html lang="en">
<head>
<meta charset="utf-8">
<title>Tidal Sway – Flyer</title>
<link href="https://fonts.googleapis.com/css2?family=Arimo:wght@400;700&family=Poppins:wght@700;800&display=swap" rel="stylesheet">
<style>
  :root {
    --violet-deep: #2a1466;
    --violet: #6b2fd0;
    --lilac: #b07cf5;
    --sky: #4d7ee8;
    --lime: #c6f21e;
    --magenta: #ff1fb0;
    --title-pink: #e3179a;
    --white: #ffffff;
    --band: rgba(255, 255, 255, 0.22);
  }
  * { box-sizing: border-box; margin: 0; padding: 0; }
  html, body { width: 1200px; height: 831px; overflow: hidden; background: var(--violet-deep); }
  .flyer {
    position: relative;
    width: 1200px;
    height: 831px;
    overflow: hidden;
    font-family: "Arimo", Arial, sans-serif;
    color: var(--white);
  }
  .backdrop {
    position: absolute;
    inset: 0;
    background:
      radial-gradient(ellipse 420px 260px at 90px 760px, var(--lime) 0%, rgba(198, 242, 30, 0.6) 45%, rgba(198, 242, 30, 0) 100%),
      radial-gradient(circle 430px at 720px 420px, rgba(20, 10, 60, 0.85) 0%, rgba(40, 20, 110, 0.55) 60%, rgba(40, 20, 110, 0) 100%),
      radial-gradient(ellipse 500px 380px at 1150px 200px, var(--lilac) 0%, rgba(176, 124, 245, 0) 100%),
      radial-gradient(ellipse 460px 360px at 200px 120px, var(--sky) 0%, rgba(77, 126, 232, 0) 100%),
      linear-gradient(160deg, var(--violet) 0%, var(--violet-deep) 55%, var(--violet) 100%);
  }
  .side-band {
    position: absolute;
    left: 0;
    top: 0;
    width: 120px;
    height: 831px;
    background: var(--band);
  }
  .side-band__name {
    position: absolute;
    left: 60px;
    top: 415px;
    transform: translate(-50%, -50%) rotate(-90deg);
    white-space: nowrap;
    font-family: "Poppins", Arial, sans-serif;
    font-weight: 800;
    font-size: 70px;
    letter-spacing: 2px;
    color: var(--white);
  }
  .title {
    position: absolute;
    left: 300px;
    top: 72px;
    padding: 6px 24px 4px;
    background: var(--title-pink);
    transform: rotate(-4deg);
    font-family: "Poppins", Arial, sans-serif;
    font-weight: 800;
    font-size: 70px;
    line-height: 1.1;
    color: var(--white);
    white-space: nowrap;
  }
  .copy {
    position: absolute;
    left: 360px;
    width: 790px;
    text-align: center;
    font-size: 20.5px;
    line-height: 27px;
    text-shadow: 0 0 4px rgba(20, 10, 60, 0.6);
  }
  .copy--intro { top: 154px; }
  .copy--about-class { top: 343px; }
  .copy--bio { top: 458px; }
  .copy--contact { top: 643px; }
  .copy--tagline { top: 722px; }
  .accent { color: var(--magenta); font-weight: 700; }
  .heading { display: block; color: var(--magenta); font-weight: 700; }
  .email { font-weight: 700; }
</style>
</head>
<body>
<div class="flyer">
  <div class="backdrop" role="img" aria-label="Silhouettes of two dancers leaping across bursting light rays in violet, blue and lime green"></div>

  <div class="side-band">
    <span class="side-band__name">TIDAL SWAY</span>
  </div>

  <h1 class="title">TIDAL SWAY</h1>

  <p class="copy copy--intro">
    &nbsp;&nbsp;&nbsp;&nbsp;&nbsp;&nbsp;&nbsp;&nbsp;&nbsp;&nbsp;&nbsp;&nbsp;&nbsp;&nbsp;&nbsp;&nbsp;&nbsp;&nbsp;&nbsp;&nbsp;&nbsp;&nbsp;&nbsp;&nbsp;&nbsp;&nbsp;&nbsp;&nbsp;&nbsp;&nbsp;&nbsp;&nbsp;&nbsp;&nbsp;&nbsp;&nbsp;&nbsp;&nbsp;&nbsp;We need to move.<br>
    &nbsp;&nbsp;&nbsp;&nbsp;&nbsp;&nbsp;&nbsp;&nbsp;&nbsp;&nbsp;&nbsp;&nbsp;We need to breathe. We need to smile and giggle<br>
    and laugh and cry and scream and make noise and dance. It's not about<br>
    burning calories and it is not about reaching a goal. It's about feeling. It's<br>
    about taking the time to nurture our souls. It's about finding joy and peace in<br>
    our hectic lives. It's about healing.
  </p>

  <p class="copy copy--about-class">
    <span class="accent">Tidal Sway</span> is a wildly fun, uplifting, emotionally cleansing, refreshing, restorative,<br>
    heart-opening, transformational dance celebration that is sure to leave you relaxed<br>
    and smiling. All ages, shapes and sizes are welcome with no experience necessary.
  </p>

  <p class="copy copy--bio">
    <span class="heading">About Nora:</span>
    I was certified at Venduro in both “Move Through Morning” and “Orbit Motion” and am<br>
    a certified Group Exercise Instructor with the Cardio and Wellness Guild of Northland<br>
    (CWGN). I also have a black belt in Tae Kwon Do. As of 2013, I will be a<br>
    certified holistic health and nutrition coach and am the creator of the popular<br>
    Bright, Brisk, and Bold page on Chatterbook.
  </p>

  <p class="copy copy--contact">
    <span class="heading">For more info:</span>
    <span class="email">Noradekker@mailquill.com</span>
  </p>

  <p class="copy copy--tagline">
    Classes and workshops to energize your body, mind,<br>
    and spirit.
  </p>
</div>
</body>
</html>
```